Summer Sale Graphics for Social Media

I want to create 11 social media graphics (new Instagram size 4:5 (1080 x 1350 pixels) focusing on our Summer Sale Graphics, using any of the pics attached. Use the attached pics, NO RANDOM STOCK PHOTOGRAPHY. For the color scheme of the graphics, they should all be complementary to the product colors in the photos.
You can add any of the photos attached but none are required. You can do some of the graphics in all text. I mainly need BOLD text that says one of the headlines (11 total) SEE ATTACHED WORD DOCUMENT for the headlines to use.

```html
<!DOCTYPE html>
<html lang="en">
<head>
<meta charset="utf-8">
<title>Summer Sale</title>
<link rel="stylesheet" href="https://fonts.googleapis.com/css2?family=Anton&display=swap">
<style>
  :root {
    --magenta: #b04f86;
    --magenta-deep: #9c3f73;
    --pink-light: #d47aa1;
    --pink-glow: #eaa2c8;
    --panel: #e2e2e0;
    --panel-light: #ececeb;
    --frame-top: #b35388;
    --frame-bottom: #d2c3ca;
    --line: #c98fab;
    --white: #ffffff;
    --bottle-blue: #c9d3ea;
    --bottle-teal: #c3ddd4;
    --bottle-red: #efc9cb;
    --bottle-pink: #e8c6dc;
  }
  * { margin: 0; padding: 0; box-sizing: border-box; }
  html, body { width: 844px; height: 1200px; overflow: hidden; }
  body {
    position: relative;
    background: linear-gradient(180deg, var(--frame-top) 0%, var(--frame-top) 35%, var(--frame-bottom) 100%);
    font-family: "Anton", "Oswald", sans-serif;
  }
  .panel {
    position: absolute;
    left: 19px; top: 23px;
    width: 806px; height: 1154px;
    background: radial-gradient(ellipse 75% 45% at 55% 62%, var(--panel-light) 0%, var(--panel) 100%);
    overflow: hidden;
  }
  .decor { position: absolute; inset: 0; }
  .product-photo {
    position: absolute;
    left: 43px; top: 520px;
    width: 716px; height: 450px;
    background:
      linear-gradient(180deg, rgba(236,236,235,0) 0%, rgba(236,236,235,0) 55%, rgba(236,236,235,0.9) 100%),
      linear-gradient(90deg, var(--bottle-blue) 0%, var(--bottle-teal) 28%, var(--bottle-red) 58%, var(--bottle-pink) 100%);
    -webkit-mask-image: radial-gradient(ellipse 52% 50% at 50% 55%, #000 60%, transparent 100%);
    mask-image: radial-gradient(ellipse 52% 50% at 50% 55%, #000 60%, transparent 100%);
  }
  .headline {
    position: absolute;
    left: 0; right: 0; top: 86px;
    text-align: center;
    color: var(--magenta);
    font-size: 96px;
    line-height: 97px;
    letter-spacing: -1.5px;
    font-weight: 400;
  }
  .cta {
    position: absolute;
    left: 234px; top: 330px;
    width: 338px; height: 75px;
    border-radius: 38px;
    background: var(--magenta);
    box-shadow: 0 0 0 4px var(--pink-glow), inset 0 0 10px rgba(255,255,255,0.25);
    color: var(--white);
    font-size: 42px;
    line-height: 75px;
    text-align: center;
    letter-spacing: 0.3px;
  }
  .badge {
    position: absolute;
    left: 37px; top: 797px;
    width: 200px; height: 200px;
  }
  .badge svg { position: absolute; inset: 0; }
  .badge-text {
    position: absolute;
    inset: 0;
    display: flex; flex-direction: column; align-items: center; justify-content: center;
    color: var(--white);
    text-align: center;
  }
  .badge-small { font-size: 33px; line-height: 38px; }
  .badge-big { font-size: 52px; line-height: 50px; }
</style>
</head>
<body>
  <main class="panel">
    <svg class="decor" width="806" height="1154" viewBox="0 0 806 1154" aria-hidden="true">
      <g fill="none" stroke="var(--line)" stroke-width="1">
        <circle cx="0" cy="402" r="134"/>
        <circle cx="0" cy="402" r="119"/>
        <circle cx="806" cy="489" r="120"/>
        <circle cx="806" cy="489" r="103"/>
      </g>
    </svg>

    <div class="product-photo" role="img" aria-label="Photo of four white supplement bottles with blue, teal, red and pink labels standing in a row"></div>

    <svg class="decor" width="806" height="1154" viewBox="0 0 806 1154" aria-hidden="true">
      <path d="M0 974 C 200 1045, 480 1000, 806 944 V1154 H0 Z" fill="var(--pink-light)"/>
      <path d="M0 1033 C 220 1075, 450 1012, 806 958 V1154 H0 Z" fill="var(--magenta)"/>
      <g fill="none" stroke="var(--line)" stroke-width="1">
        <circle cx="775" cy="1121" r="94"/>
        <circle cx="775" cy="1121" r="80"/>
      </g>
    </svg>

    <h1 class="headline">Your Summer Body<br>Won’t Wait –</h1>
    <div class="cta">SALE NOW!</div>

    <div class="badge">
      <svg width="200" height="200" viewBox="-100 -100 200 200" aria-hidden="true">
        <defs>
          <linearGradient id="badgeFill" x1="0" y1="0" x2="0" y2="1">
            <stop offset="0" stop-color="#c86a9c"/>
            <stop offset="1" stop-color="#a13f76"/>
          </linearGradient>
        </defs>
        <polygon fill="url(#badgeFill)" stroke="var(--magenta-deep)" stroke-width="1.5"
          points="97,0 79.2,21.2 84,48.5 58,58 48.5,84 21.2,79.2 0,97 -21.2,79.2 -48.5,84 -58,58 -84,48.5 -79.2,21.2 -97,0 -79.2,-21.2 -84,-48.5 -58,-58 -48.5,-84 -21.2,-79.2 0,-97 21.2,-79.2 48.5,-84 58,-58 84,-48.5 79.2,-21.2"/>
        <polygon fill="none" stroke="#e7a9c9" stroke-width="1" transform="scale(0.9)"
          points="97,0 79.2,21.2 84,48.5 58,58 48.5,84 21.2,79.2 0,97 -21.2,79.2 -48.5,84 -58,58 -84,48.5 -79.2,21.2 -97,0 -79.2,-21.2 -84,-48.5 -58,-58 -48.5,-84 -21.2,-79.2 0,-97 21.2,-79.2 48.5,-84 58,-58 84,-48.5 79.2,-21.2"/>
      </svg>
      <div class="badge-text">
        <span class="badge-small">Up to</span>
        <span class="badge-big">$15</span>
        <span class="badge-big">OFF</span>
      </div>
    </div>
  </main>
</body>
</html>
```